Roll-UP

Urgent and easy mission
I need the HD material for a roll-up

Instructions:
-Use the attached psd file: the back of my business card
-Make something similar to this (same colors and layout) but in another size. For a roll-up banner of 85 cmx200 cm high
-The logo shall be in the center of the banner.
-And take into account the instructions from the supplier regarding the preparation of the HD file that I will need to upload on their online platform. See link hereunder from the supplier.
http://www.velmorprint.example/displays/roller-banners/classic-mono/
(Tips for the preparation and printing of your file
You should send us a PDF, JPEG or TIFF file with the following features:
Base: 85.2 cm
Height: 220.2 cm
Use the template to create your file correctly. Without crop marks)
-Please send it in psd and pdf

Printing

```html
<!DOCTYPE html>
<html lang="en">
<head>
<meta charset="utf-8">
<title>Marlow Cranes – Roll-up Banner</title>
<link rel="stylesheet" href="https://fonts.googleapis.com/css2?family=Roboto:wght@300&family=Lato:wght@700&display=swap">
<style>
  :root {
    --banner-blue: #15467c;
    --accent-orange: #f08a24;
    --band-white: #ffffff;
    --url-navy: #1d3f70;
    --text-white: #ffffff;
  }
  html, body {
    margin: 0;
    padding: 0;
    width: 1200px;
    height: 3103px;
    overflow: hidden;
    background: var(--banner-blue);
  }
  .roll-up {
    position: relative;
    width: 1200px;
    height: 3103px;
    background: var(--banner-blue);
    overflow: hidden;
  }
  .brand-mark {
    position: absolute;
    left: 420px;
    top: 760px;
    width: 360px;
    height: 360px;
    border-radius: 50%;
    background: var(--text-white);
  }
  .brand__name,
  .brand__tagline {
    position: absolute;
    left: 0;
    right: 0;
    margin: 0;
    text-align: center;
    color: var(--text-white);
    font-family: "Roboto", Arial, sans-serif;
    font-weight: 300;
    line-height: 1;
    white-space: nowrap;
  }
  .brand__name {
    top: 1265px;
    font-size: 124px;
    letter-spacing: 0;
  }
  .brand__tagline {
    top: 1430px;
    font-size: 83px;
    letter-spacing: 1px;
  }
  .web-band {
    position: absolute;
    left: 0;
    top: 2133px;
    width: 1200px;
    height: 500px;
  }
  .web-band svg {
    display: block;
  }
  .web-band__url {
    position: absolute;
    left: 0;
    right: 0;
    top: 0;
    height: 500px;
    margin: 0;
    display: flex;
    align-items: center;
    justify-content: center;
    font-family: "Lato", Arial, sans-serif;
    font-weight: 700;
    font-size: 58px;
    letter-spacing: 2px;
    color: var(--url-navy);
  }
</style>
</head>
<body>
  <main class="roll-up">
    <div class="brand-mark" role="img" aria-label="Marlow Cranes bird symbol"></div>
    <h1 class="brand__name">MARLOW CRANES</h1>
    <p class="brand__tagline">TRAVEL RETAIL</p>

    <section class="web-band">
      <svg width="1200" height="500" viewBox="0 0 1200 500" aria-hidden="true">
        <ellipse cx="600" cy="250" rx="900" ry="215" fill="var(--accent-orange)"/>
        <ellipse cx="600" cy="250" rx="830" ry="211" fill="var(--banner-blue)"/>
        <ellipse cx="600" cy="250" rx="700" ry="176" fill="var(--band-white)"/>
      </svg>
      <p class="web-band__url">www.marlowcranes.example</p>
    </section>
  </main>
</body>
</html>
```